Beautiful Simple and Clean WEbsite for Life Coach

Looking for a simple clean site website for life coach for educators. A home page will have an embedded opt-in form, menu bar will be
Work With Me - page for my coaching program and link to online calendar for booking
PRAISE - testimonials
ABOUT
PODCAST
I can supply images and a site I would like it modeled after is https://petrawendt.com/
My current website at www.dorabeckett.com is too dark. I am looking for the white space, pink and magenta. Feel free to use images from the site

Industry/Entity Type

Life Coaching

Number of Pages Required

4 page

Font styles to use
Serif

Colors
E54698
E96AAD
F1A4CE
F9D9EA
FCEFF6

Requirements
Must have
• See attached files for must-haves, Lots of white space, opt-in from for freebie is the most prominent on home page
Nice to have
• refer to Petra Wendt websites
Should not have
• dark colors, any balck background

```html
<!DOCTYPE html>
<html lang="en">
<head>
<meta charset="utf-8">
<title>Dora Beckett – Life Coach for Educators</title>
<link href="https://fonts.googleapis.com/css2?family=Playfair+Display:wght@400;500&family=Montserrat:wght@400;500;600&display=swap" rel="stylesheet">
<style>
:root{
  --magenta:#E54698;
  --pink:#E96AAD;
  --pink-mid:#F1A4CE;
  --pink-soft:#F9D9EA;
  --pink-pale:#FCEFF6;
  --hero-panel:#FBD3CF;
  --button:#F3A9B6;
  --mauve:#9C7985;
  --testimonial-bg:#F6BCCF;
  --footer-bg:#FCE3DA;
  --ink:#1F1F1F;
  --text:#5A5A5A;
  --white:#FFFFFF;
  --serif:"Playfair Display", Georgia, serif;
  --sans:"Montserrat", Arial, sans-serif;
}
*{box-sizing:border-box;margin:0;padding:0}
html,body{width:1200px;height:5012px;overflow:hidden;background:var(--white)}
body{position:relative;font-family:var(--sans);color:var(--text)}
.abs{position:absolute}
.btn{position:absolute;background:var(--button);color:var(--white);font:600 14px/1 var(--sans);letter-spacing:1.5px;text-transform:uppercase;display:flex;align-items:center;justify-content:center}
.btn-outline{background:var(--white);color:var(--button);border:2px solid var(--button);box-shadow:0 0 0 4px var(--white),0 0 0 5px var(--pink-soft)}
.photo{position:absolute}
.eyebrow{font:400 19px/1 var(--serif);letter-spacing:1.5px;text-transform:uppercase;color:var(--ink)}
.section-title{font:400 40px/1.1 var(--serif);letter-spacing:2px;text-transform:uppercase;color:var(--ink)}

/* header */
.site-header{position:absolute;left:0;top:0;width:1200px;height:100px;z-index:5}
.brand{left:78px;top:34px;font:400 40px/1 var(--serif);color:var(--pink-mid)}
.main-nav{left:652px;top:44px;display:flex;gap:50px;font:500 15px/1 var(--sans);letter-spacing:1.5px;color:#444}

/* hero */
.hero-photo{left:600px;top:100px;width:600px;height:560px;background:linear-gradient(135deg,#D9C8A5 0%,#EFE3D6 45%,#F6F1EC 70%,#C9D7E3 100%)}
.hero-panel{left:0;top:140px;width:620px;height:520px;background:var(--hero-panel)}
.hero-title{left:92px;top:180px;font:400 52px/1.1 var(--serif);letter-spacing:3px;color:var(--ink)}
.hero-sub{left:92px;top:322px;width:480px;font:400 16px/1.6 var(--sans);color:#4A4A4A}
.field{position:absolute;top:436px;width:200px;border-bottom:1px solid #9B8B88;padding-bottom:10px;font:400 15px/1 var(--sans);color:#555}

/* freebie */
.freebie{left:0;top:780px;width:1200px;text-align:center}
.freebie .eyebrow{font-size:18px}
.freebie .section-title{margin-top:14px}
.freebie p{width:620px;margin:22px auto 0;font:400 17px/1.6 var(--sans)}

/* about */
.about{left:0;top:1180px;width:1200px;height:840px;background:var(--mauve)}
.about-photo{left:88px;top:120px;width:400px;height:572px;border:6px solid var(--white);background:linear-gradient(180deg,#B9A58A 0%,#D8CDB9 40%,#E9E4DA 60%,#7E8C5A 100%)}
.about-copy{left:588px;top:116px;width:520px;color:var(--white)}
.about-copy .eyebrow{color:var(--white);font-size:20px}
.about-copy h2{font:400 40px/1.2 var(--serif);letter-spacing:2px;margin-top:6px}
.about-copy p{font:400 16px/1.7 var(--sans);margin-top:28px}

/* imagine */
.imagine-head{left:0;top:2118px;width:1200px;text-align:center}
.imagine-head .section-title{margin-top:10px}
.row-title{font:500 22px/1.35 var(--serif);letter-spacing:1px;text-transform:uppercase;color:var(--ink)}
.row-text{font:400 16px/1.7 var(--sans);color:var(--text)}
.icon-badge{position:absolute;width:96px;height:96px;border-radius:50%;background:var(--white);box-shadow:0 4px 14px rgba(0,0,0,.12);display:flex;align-items:center;justify-content:center}
.stage-list{list-style:none}
.stage-list li{position:relative;padding-left:30px;margin-bottom:26px;font:400 16px/1.6 var(--sans)}
.stage-list li::before{content:"";position:absolute;left:0;top:6px;width:14px;height:14px;border-radius:50%;background:var(--pink-mid)}

/* testimonials */
.testimonials{left:0;top:3620px;width:1200px;height:720px;background:var(--testimonial-bg)}
.testimonials-head{left:0;top:130px;width:1200px;text-align:center}
.testimonials-head .section-title{margin-top:8px}
.testimonials-head .rule{width:80px;height:2px;background:var(--ink);margin:18px auto 0}
.quote-card{position:absolute;top:260px;width:486px;height:420px;background:var(--white);padding:40px 40px}
.quote-mark{font:700 64px/0.8 var(--serif);color:var(--pink)}
.quote-card p{font:400 17px/1.6 var(--sans);margin-top:14px;color:#555}
.quote-card .name{margin-top:26px;font:500 16px/1 var(--serif);letter-spacing:1px;text-transform:uppercase;color:var(--ink)}
.stars{margin-top:12px;display:flex;gap:6px}
.slider-arrow{position:absolute;top:334px;width:56px;height:56px;border-radius:50%;background:#8E8E8E;display:flex;align-items:center;justify-content:center}

/* call band */
.call-band{left:0;top:4340px;width:1200px;height:220px;background:var(--white)}
.call-photo{left:0;top:0;width:460px;height:220px;background:linear-gradient(90deg,#E8DCD6 0%,#F4EEEB 55%,rgba(255,255,255,0) 100%)}
.call-title{left:90px;top:74px;font:400 28px/1.2 var(--serif);letter-spacing:1.5px;text-transform:uppercase;color:var(--ink)}
.call-divider{left:500px;top:46px;width:1px;height:128px;background:#BDBDBD}
.call-text{left:540px;top:54px;width:380px;font:400 16px/1.7 var(--sans)}

/* footer */
.site-footer{left:0;top:4560px;width:1200px;height:452px;background:var(--footer-bg);text-align:center}
.footer-brand{margin-top:78px;font:400 40px/1 var(--serif);color:var(--pink-mid)}
.footer-nav{margin-top:58px;display:flex;justify-content:center;gap:54px;font:500 15px/1 var(--sans);letter-spacing:1.5px;color:#444}
.social{margin-top:44px;display:flex;justify-content:center;gap:18px}
.social span{width:44px;height:44px;border-radius:50%;background:#C9B0AE}
.legal{margin-top:26px;display:flex;justify-content:center;gap:34px;font:400 14px/1 var(--sans);color:#444}
.copyright{margin-top:54px;font:400 14px/1 var(--sans);color:#555}
</style>
</head>
<body>

<header class="site-header">
  <div class="abs brand">Dora Beckett</div>
  <nav class="abs main-nav"><span>WORK WITH ME</span><span>PRAISE</span><span>ABOUT</span><span>PODCAST</span></nav>
</header>

<section class="hero">
  <div class="photo hero-photo" role="img" aria-label="Smiling coach in a wide-brimmed sun hat reading a book outdoors"></div>
  <div class="abs hero-panel"></div>
  <h1 class="abs hero-title">LIFE COACH FOR<br>EDUCATORS</h1>
  <p class="abs hero-sub">Being Overworked, being Overwhelmed and not having Work - Life Balance and Want LESS Stress.</p>
  <div class="field" style="left:92px">Name</div>
  <div class="field" style="left:352px">Email Address</div>
  <div class="btn" style="left:92px;top:514px;width:226px;height:52px">LET YOU TELL ME !</div>
</section>

<section class="abs freebie">
  <div class="eyebrow">WHY SCHOOL LEADERS NEED BALANCE TO SUCCEED</div>
  <h2 class="section-title">THE 5 STEPS TO MAKE IT HAPPEN</h2>
  <p>DISCOVER the secrets on how to prioritize the items on an overwhelming to-do list to get the job done successfully.</p>
  <div class="btn btn-outline" style="left:552px;top:218px;width:320px;height:48px;position:absolute">DOWNLOAD THE FREE GUIDE</div>
</section>

<section class="abs about">
  <div class="photo about-photo" role="img" aria-label="Coach standing in an arched garden doorway"></div>
  <div class="abs about-copy">
    <div class="eyebrow">ABOUT ME</div>
    <h2>HI, I'M DORA BECKETT!</h2>
    <p>I'm a Life Coach. I am also a retired Elementary School Principal who loves other educators and everything in education.</p>
    <p>In my coaching practice, I empower my clients with simple survival skills to succeed at their school and in their life. They have more time, less stress, and yell less.</p>
    <p>If you would like to learn more about how to manage stress and overwhelm, and how to feel better no matter what the circumstances I am your gal.</p>
  </div>
  <div class="btn" style="left:588px;top:640px;width:208px;height:52px">MORE ABOUT US</div>
</section>

<section class="imagine">
  <div class="abs imagine-head">
    <div class="eyebrow">IMAGINATION</div>
    <h2 class="section-title">IMAGINE A LIFE WHERE...</h2>
  </div>

  <svg class="abs" style="left:0;top:2500px" width="1200" height="760" viewBox="0 0 1200 760" aria-hidden="true">
    <path d="M780 100 V260 H280 V230" fill="none" stroke="#9A9A9A" stroke-width="2" stroke-dasharray="6 6"/>
    <path d="M472 420 V540 H900 V680" fill="none" stroke="#9A9A9A" stroke-width="2" stroke-dasharray="6 6"/>
  </svg>

  <h3 class="abs row-title" style="left:88px;top:2328px;width:560px">AT THE END OF THIS LIFE YOU LOOK BACK &amp; ADMIRE WHO YOU WERE AS A LEADER.</h3>
  <p class="abs row-text" style="left:88px;top:2410px;width:560px">You are your best for the world and yourself/Family, those at work, and friends receive more and the best of you. Anxiety, worry, and fear are no more. It feels happy and calm to have an extraordinary life of purpose and powerful leadership.</p>
  <div class="photo" style="left:732px;top:2280px;width:372px;height:320px;background:linear-gradient(180deg,#F2B347 0%,#E58A2E 55%,#6B4A3A 100%)" role="img" aria-label="Woman with open arms at sunset by the sea"></div>
  <div class="icon-badge" style="left:684px;top:2392px"><svg width="44" height="44" viewBox="0 0 44 44"><circle cx="22" cy="14" r="7" fill="none" stroke="#E96AAD" stroke-width="2.5"/><path d="M8 38c2-9 8-13 14-13s12 4 14 13" fill="none" stroke="#E96AAD" stroke-width="2.5"/></svg></div>

  <div class="photo" style="left:88px;top:2712px;width:384px;height:328px;background:linear-gradient(135deg,#6E5A4C 0%,#B89A86 50%,#8D7A6E 100%)" role="img" aria-label="Smiling young woman in a casual sweater"></div>
  <div class="icon-badge" style="left:420px;top:2824px"><svg width="44" height="44" viewBox="0 0 44 44"><rect x="9" y="6" width="26" height="32" rx="3" fill="none" stroke="#E96AAD" stroke-width="2.5"/><path d="M15 16h14M15 23h14M15 30h9" stroke="#E96AAD" stroke-width="2.5"/></svg></div>
  <h3 class="abs row-title" style="left:580px;top:2776px;width:460px">TOGETHER WE CAN MAKE THIS LIFE A REALITY FOR YOU</h3>
  <p class="abs row-text" style="left:580px;top:2866px;width:520px">It's possible and I will show you how! I am that person to help you get different results for your problems as we figure out the root causes.</p>

  <h3 class="abs row-title" style="left:88px;top:3150px">THE 5 STAGES OF GETTING RESULTS</h3>
  <ul class="abs stage-list row-text" style="left:88px;top:3206px;width:560px">
    <li>Being aware of the circumstances of our problem and which voice in our head is causing it</li>
    <li>Being honest about our thoughts</li>
    <li>Allowing feelings without judgement or resistance</li>
    <li>Being in massive action to shift into wisdom or sage mode.</li>
    <li>Based on results fail, learn, and try again</li>
  </ul>
  <div class="photo" style="left:732px;top:3180px;width:376px;height:320px;background:linear-gradient(180deg,#C7D3DA 0%,#E7E9E6 55%,#3F3A38 100%)" role="img" aria-label="Woman in a yoga pose on a seaside deck"></div>
  <div class="icon-badge" style="left:684px;top:3196px"><svg width="44" height="44" viewBox="0 0 44 44"><rect x="8" y="8" width="28" height="28" rx="3" fill="none" stroke="#E96AAD" stroke-width="2.5"/><path d="M14 24l6 6 11-13" fill="none" stroke="#E96AAD" stroke-width="2.5"/></svg></div>
</section>

<section class="abs testimonials">
  <div class="abs testimonials-head">
    <div class="eyebrow">TESTIMONIAL</div>
    <h2 class="section-title">WHAT MY CLIENTS SAY...</h2>
    <div class="rule"></div>
  </div>
  <div class="slider-arrow" style="left:20px"><svg width="20" height="20" viewBox="0 0 20 20"><path d="M12 4l-6 6 6 6" fill="none" stroke="#fff" stroke-width="2.5"/></svg></div>
  <article class="quote-card" style="left:88px">
    <div class="quote-mark">“</div>
    <p>Lorem ipsum dolor sit amet consectetur adipisicing elit sed do eiusmod tempor incididunt ut labore et dolore magna aliqua. Ut enim ad minim veniam quis nostrud exercitation ullamco.</p>
    <div class="name">SOPHIE LAROUX</div>
    <div class="stars"><svg width="110" height="18" viewBox="0 0 110 18" fill="#8E7F86"><g id="star"><path d="M9 1l2.4 5.2 5.6.6-4.2 3.8 1.2 5.5L9 13.3 4 16.1l1.2-5.5L1 6.8l5.6-.6z"/></g><use href="#star" x="22"/><use href="#star" x="44"/><use href="#star" x="66"/><use href="#star" x="88"/></svg></div>
  </article>
  <article class="quote-card" style="left:612px">
    <div class="quote-mark">“</div>
    <p>Lorem ipsum dolor sit amet consectetur adipisicing elit sed do eiusmod tempor incididunt ut labore et dolore magna aliqua. Ut enim ad minim veniam quis nostrud exercitation ullamco.</p>
    <div class="name">SOPHIE LAROUX</div>
    <div class="stars"><svg width="110" height="18" viewBox="0 0 110 18" fill="#8E7F86"><use href="#star"/><use href="#star" x="22"/><use href="#star" x="44"/><use href="#star" x="66"/><use href="#star" x="88"/></svg></div>
  </article>
  <div class="slider-arrow" style="left:1124px"><svg width="20" height="20" viewBox="0 0 20 20"><path d="M8 4l6 6-6 6" fill="none" stroke="#fff" stroke-width="2.5"/></svg></div>
</section>

<section class="abs call-band">
  <div class="photo call-photo" role="img" aria-label="Faded portrait of the coach"></div>
  <h2 class="abs call-title">BOOK A MINDSET<br>RESET CALL</h2>
  <div class="abs call-divider"></div>
  <p class="abs call-text">Talk with Dora and get your questions answered, receive more personal attention, and information. Let's meet and I will help you.</p>
  <div class="btn" style="left:928px;top:88px;width:176px;height:52px">BOOK NOW</div>
</section>

<footer class="abs site-footer">
  <div class="footer-brand">Dora Beckett</div>
  <nav class="footer-nav"><span>WORK WITH ME</span><span>PRAISE</span><span>ABOUT</span><span>PODCAST</span></nav>
  <div class="social"><span></span><span></span><span></span><span></span><span></span></div>
  <div class="legal"><span>Disclaimer</span><span>Privacy Policy</span><span>Terms Of use</span></div>
  <div class="copyright">Copyright © 2022 Dora Beckett. All Rights Reserved</div>
</footer>

</body>
</html>
```